Morevo - Augmented Reality Mobile application

We need a logo design for new mobile application. The overall objective of the application is to build a digital content delivery tool for scanning and recognizing of an image (marker) through a mobile application. The provision of digital content to the user takes place via augmeted reality and / or redirecting the user to a given digital content source.We don`t have any color scheme yet, but we have been thinking about something colorful. We are open for ideas.I have uploaded our working logos, but we are not strongly engaged with them.
Updates

Hello everybody, I have increased the budget of the project Regards

Target Market(s)

Entertainment; Education;

Industry/Entity Type

Entertainment

Logo Text

"Morevo" is the name of the product. We want a logo enough distinguishable to be recognized even without the text

Font styles to use
Serif
Sans Serif

Colors

Designer to choose colors to be used in the design.

Requirements
Must have
• We have attached a document with some information about the product. Feel free to use whatever found useful in it.
• We are not looking for the same design, rather an alternative one. We need all of the screens mentioned in the document
Nice to have
Should not have

```html
<!DOCTYPE html>
<html lang="en">
<head>
<meta charset="utf-8">
<title>Morevo – App Screens</title>
<link href="https://fonts.googleapis.com/css2?family=Montserrat:wght@500;600;700&family=Open+Sans:wght@400;600&display=swap" rel="stylesheet">
<style>
:root{
  --bg:#f8f7f6;
  --orange:#ff6a10;
  --orange-light:#ff9a55;
  --red:#f2410f;
  --blue:#2f65c9;
  --ink:#2b2b2b;
  --muted:#555;
  --tab:#eeeeee;
  --white:#ffffff;
}
*{box-sizing:border-box;margin:0;padding:0}
html,body{width:798px;height:1200px;overflow:hidden;background:var(--bg)}
body{position:relative;font-family:"Open Sans",sans-serif;color:var(--ink)}
.screen{position:absolute;width:152px;height:270px;background:var(--white);overflow:hidden;box-shadow:0 2px 8px rgba(0,0,0,.08)}
.app-bar{height:23px;background:var(--blue);color:var(--white);display:flex;align-items:center;justify-content:space-between;padding:0 7px}
.app-bar h2{font-family:"Montserrat",sans-serif;font-weight:600;font-size:8px;letter-spacing:.3px}
.app-bar svg{width:10px;height:10px}
.tagline{position:absolute;left:0;right:0;bottom:12px;text-align:center;font-family:"Montserrat",sans-serif;font-weight:500;font-size:9px;color:var(--ink)}
/* splash */
.splash{background:linear-gradient(160deg,var(--orange-light) 0%,var(--orange) 55%,#ff7a1e 100%)}
.splash::before{content:"";position:absolute;inset:0;background:linear-gradient(120deg,rgba(255,255,255,.0) 45%,rgba(255,255,255,.08) 45%)}
.corner-icon{position:absolute;top:8px;width:12px;height:12px}
.brand{position:absolute;top:88px;left:0;right:0;text-align:center;font-family:"Montserrat",sans-serif;font-weight:500;font-size:23px;color:var(--white)}
.brand-mark{display:block;width:12px;height:12px;margin:0 auto 6px;background:var(--white)}
.btn{position:absolute;left:21px;width:110px;height:28px;border-radius:14px;color:var(--white);font-family:"Montserrat",sans-serif;font-weight:600;font-size:9px;display:flex;align-items:center;padding-left:13px;gap:8px;box-shadow:0 2px 4px rgba(0,0,0,.15)}
.btn svg{width:13px;height:13px}
.btn-scan{top:145px;background:var(--red)}
.btn-how{top:179px;background:var(--blue)}
.splash .tagline{color:var(--white)}
/* tabs */
.tabs{display:flex;height:23px;background:var(--tab)}
.tab{flex:1;display:flex;align-items:center;justify-content:center;font-size:7px;color:var(--ink)}
.tab.active{color:var(--orange);border-bottom:2px solid var(--orange);background:var(--white)}
.about-copy{padding:9px 11px 0;font-size:6.3px;line-height:10px;color:var(--ink)}
.about-copy p+p{margin-top:10px}
.contact-list{padding:12px 0 0 18px;list-style:none}
.contact-list li{display:flex;gap:6px;font-size:6.3px;line-height:10px;margin-bottom:6px}
.contact-list svg{width:9px;height:9px;flex:none;margin-top:1px}
.contact-list b{font-weight:600}
/* how to */
.step-badge{position:absolute;left:33px;top:38px;width:86px;height:86px;border-radius:50%;border:1.5px solid var(--orange);display:flex;align-items:center;justify-content:center}
.step-badge svg{width:56px;height:56px}
.step-title{position:absolute;top:148px;left:0;right:0;text-align:center;font-family:"Montserrat",sans-serif;font-weight:700;font-size:9px;color:var(--orange)}
.step-copy{position:absolute;top:162px;left:13px;right:13px;text-align:center;font-size:6.3px;line-height:10px;color:var(--ink)}
.pager{position:absolute;bottom:14px;left:63px;display:flex;gap:3px}
.pager i{width:5px;height:5px;border-radius:50%;background:#bbb}
.pager i.on{background:#555}
.next{position:absolute;right:9px;bottom:12px;width:11px;height:9px}
/* scan */
.scan-tools{display:flex;justify-content:center;gap:21px;margin-top:12px}
.scan-tools span{width:13px;height:13px;border-radius:50%;display:flex;align-items:center;justify-content:center}
.scan-tools svg{width:8px;height:8px}
.scan-ring{position:absolute;left:16px;top:89px;width:120px;height:120px}
.scan-label{position:absolute;left:0;right:0;top:143px;text-align:center;font-family:"Montserrat",sans-serif;font-weight:700;font-size:9px;color:var(--orange)}
</style>
</head>
<body>

<!-- Home -->
<section class="screen splash" style="left:124px;top:84px">
  <svg class="corner-icon" style="left:9px" viewBox="0 0 12 12"><circle cx="6" cy="6" r="6" fill="#f2410f"/><rect x="5.3" y="5" width="1.4" height="4.5" fill="#fff"/><circle cx="6" cy="3.3" r=".9" fill="#fff"/></svg>
  <svg class="corner-icon" style="right:9px" viewBox="0 0 12 12"><circle cx="6" cy="6" r="6" fill="#f2410f"/><path d="M8.6 5.2A2.8 2.8 0 1 0 8 7.8" fill="none" stroke="#fff" stroke-width="1.2"/><path d="M9.3 3.3v2.4H6.9z" fill="#fff"/></svg>
  <div class="brand"><span class="brand-mark"></span>Morevo</div>
  <div class="btn btn-scan"><svg viewBox="0 0 14 14" fill="none" stroke="#fff" stroke-width="1.6"><path d="M1 4V1h3M10 1h3v3M13 10v3h-3M4 13H1v-3M1 7h12"/></svg>START SCAN</div>
  <div class="btn btn-how"><svg viewBox="0 0 14 14" fill="none" stroke="#fff" stroke-width="1.2"><circle cx="7" cy="7" r="6"/><path d="M5.2 5.4a1.9 1.9 0 1 1 2.6 1.7c-.6.3-.8.7-.8 1.3"/><circle cx="7" cy="10.3" r=".5" fill="#fff"/></svg>HOW TO</div>
  <p class="tagline">broden your reality</p>
</section>

<!-- About -->
<section class="screen" style="left:320px;top:84px">
  <header class="app-bar">
    <svg viewBox="0 0 10 10" fill="none" stroke="#fff" stroke-width="1"><path d="M9 5H1M4.5 1.5 1 5l3.5 3.5"/></svg>
    <h2>ABOUT</h2>
    <svg viewBox="0 0 10 10" stroke="#fff" stroke-width="1"><path d="M0 2h10M0 5h10M0 8h10"/></svg>
  </header>
  <nav class="tabs"><span class="tab active">About</span><span class="tab">Contact</span></nav>
  <div class="about-copy">
    <p>Lorem Ipsum is simply dummy text of the printing and typesetting industry. Lorem Ipsum has been the industry's standard dummy text ever since the 1500s, when an unknown printer took a galley of type and scrambled it to make a type specimen book. It has survived not only five centuries, but also the leap into electronic typesetting, remaining essentially unchanged.</p>
    <p>It was popularised in the 1960s with the release of Presset sheets containing Lorem Ipsum passages, and more recently with desktop publishing software like Pagecraft including versions of Lorem Ipsum.</p>
  </div>
  <p class="tagline">broden your reality</p>
</section>

<!-- Contact -->
<section class="screen" style="left:514px;top:85px">
  <header class="app-bar">
    <svg viewBox="0 0 10 10" fill="none" stroke="#fff" stroke-width="1"><path d="M9 5H1M4.5 1.5 1 5l3.5 3.5"/></svg>
    <h2>ABOUT</h2>
    <svg viewBox="0 0 10 10" stroke="#fff" stroke-width="1"><path d="M0 2h10M0 5h10M0 8h10"/></svg>
  </header>
  <nav class="tabs"><span class="tab">About</span><span class="tab active">Contact</span></nav>
  <ul class="contact-list">
    <li><svg viewBox="0 0 10 10"><path d="M5 10S1.5 6 1.5 3.7a3.5 3.5 0 0 1 7 0C8.5 6 5 10 5 10z" fill="#ff6a10"/><circle cx="5" cy="3.7" r="1.3" fill="#fff"/></svg><span>48 Harbor Lane, Suite 12<br>printing typesetting industry<br>Australia</span></li>
    <li><svg viewBox="0 0 10 10"><path d="M2 1l2 2-1 1.3c.6 1.2 1.5 2.1 2.7 2.7L7 6l2 2-1.2 1.2C4.5 9 1 5.5.8 2.2z" fill="#ff6a10"/></svg><span><b>800 555 0142<br>800 555 0187</b></span></li>
    <li><svg viewBox="0 0 10 10"><rect x=".5" y="2" width="9" height="6.5" fill="#ff6a10"/><path d="M.8 2.3 5 5.6l4.2-3.3" fill="none" stroke="#fff" stroke-width=".8"/></svg><span><b>info@morevo.app<br>sales@morevo.app</b></span></li>
  </ul>
  <p class="tagline">broden your reality</p>
</section>

<!-- How to: steps -->
<section class="screen" style="left:122px;top:442px">
  <header class="app-bar">
    <svg viewBox="0 0 10 10" fill="none" stroke="#fff" stroke-width="1"><path d="M9 5H1M4.5 1.5 1 5l3.5 3.5"/></svg>
    <h2>HOW TO</h2>
    <svg viewBox="0 0 10 10" stroke="#fff" stroke-width="1"><path d="M0 2h10M0 5h10M0 8h10"/></svg>
  </header>
  <div class="step-badge"><svg viewBox="0 0 24 24"><path d="M12 2l2.9 6.9 7.1.6-5.4 4.7 1.7 7.1L12 17.5l-6.3 3.8 1.7-7.1L2 9.5l7.1-.6z" fill="none" stroke="#ff6a10" stroke-width="1.4" stroke-linejoin="round"/></svg></div>
  <h3 class="step-title">STEP 1</h3>
  <p class="step-copy">Lorem Ipsum is simply dummy text of the printing and typesetting industry. Lorem Ipsum has been the industry's</p>
  <div class="pager"><i class="on"></i><i></i><i></i></div>
  <svg class="next" viewBox="0 0 11 9" fill="none" stroke="#444" stroke-width="1"><path d="M0 4.5h10M6.5 1l3.5 3.5L6.5 8"/></svg>
</section>

<section class="screen" style="left:320px;top:443px">
  <header class="app-bar">
    <svg viewBox="0 0 10 10" fill="none" stroke="#fff" stroke-width="1"><path d="M9 5H1M4.5 1.5 1 5l3.5 3.5"/></svg>
    <h2>HOW TO</h2>
    <svg viewBox="0 0 10 10" stroke="#fff" stroke-width="1"><path d="M0 2h10M0 5h10M0 8h10"/></svg>
  </header>
  <div class="step-badge"><svg viewBox="0 0 24 24"><path d="M12 2 9.1 8.9 2 9.5l5.4 4.7-1.7 7.1L12 17.5z" fill="#ff6a10"/><path d="M12 2l2.9 6.9 7.1.6-5.4 4.7 1.7 7.1L12 17.5l-6.3 3.8 1.7-7.1L2 9.5l7.1-.6z" fill="none" stroke="#ff6a10" stroke-width="1.4" stroke-linejoin="round"/></svg></div>
  <h3 class="step-title">STEP 2</h3>
  <p class="step-copy">Lorem Ipsum is simply dummy text of the printing and typesetting industry. Lorem Ipsum has been the industry's</p>
  <div class="pager"><i class="on"></i><i></i><i></i></div>
  <svg class="next" viewBox="0 0 11 9" fill="none" stroke="#444" stroke-width="1"><path d="M0 4.5h10M6.5 1l3.5 3.5L6.5 8"/></svg>
</section>

<section class="screen" style="left:516px;top:443px">
  <header class="app-bar">
    <svg viewBox="0 0 10 10" fill="none" stroke="#fff" stroke-width="1"><path d="M9 5H1M4.5 1.5 1 5l3.5 3.5"/></svg>
    <h2>HOW TO</h2>
    <svg viewBox="0 0 10 10" stroke="#fff" stroke-width="1"><path d="M0 2h10M0 5h10M0 8h10"/></svg>
  </header>
  <div class="step-badge"><svg viewBox="0 0 24 24"><path d="M12 2l2.9 6.9 7.1.6-5.4 4.7 1.7 7.1L12 17.5l-6.3 3.8 1.7-7.1L2 9.5l7.1-.6z" fill="#ff6a10" stroke="#ff6a10" stroke-width="1.4" stroke-linejoin="round"/></svg></div>
  <h3 class="step-title">STEP 3</h3>
  <p class="step-copy">Lorem Ipsum is simply dummy text of the printing and typesetting industry. Lorem Ipsum has been the industry's</p>
  <div class="pager"><i class="on"></i><i></i><i></i></div>
  <svg class="next" viewBox="0 0 11 9" fill="none" stroke="#444" stroke-width="1"><path d="M0 4.5h10M6.5 1l3.5 3.5L6.5 8"/></svg>
</section>

<!-- Scan -->
<section class="screen" style="left:124px;top:803px">
  <header class="app-bar">
    <svg viewBox="0 0 10 10" fill="none" stroke="#fff" stroke-width="1"><path d="M9 5H1M4.5 1.5 1 5l3.5 3.5"/></svg>
    <h2>SCAN</h2>
    <svg viewBox="0 0 10 10" stroke="#fff" stroke-width="1"><path d="M0 2h10M0 5h10M0 8h10"/></svg>
  </header>
  <div class="scan-tools">
    <span style="background:#ff6a10"><svg viewBox="0 0 8 8" fill="none" stroke="#fff" stroke-width="1.2"><path d="M1.5 3 4 5.5 6.5 3"/></svg></span>
    <span style="background:#3aa05a"><svg viewBox="0 0 8 8"><path d="M4.8 0 1.5 4.5h2.2L3.2 8l3.3-4.5H4.3z" fill="#fff"/></svg></span>
    <span style="background:#2196d3"><svg viewBox="0 0 8 8" fill="none" stroke="#fff" stroke-width="1"><path d="M2.6 2.8a1.4 1.4 0 1 1 1.9 1.3c-.4.2-.5.5-.5 1"/><circle cx="4" cy="6.6" r=".4" fill="#fff"/></svg></span>
  </div>
  <svg class="scan-ring" viewBox="0 0 120 120">
    <circle cx="60" cy="60" r="59" fill="none" stroke="#ffe3d2" stroke-width="1"/>
    <circle cx="60" cy="60" r="49" fill="none" stroke="#ff6a10" stroke-width="1.2"/>
    <path d="M60 11A49 49 0 0 1 108.6 66" fill="none" stroke="#ff6a10" stroke-width="3.5" stroke-linecap="round"/>
  </svg>
  <p class="scan-label">SCAN</p>
  <p class="tagline">broden your reality</p>
</section>

</body>
</html>
```